Business card design needed

I run a life coaching business.
I coach individuals, businesses & groups.
Our aim is create massive change for our clients.
I would like to see a card that is inspirational, something that provokes the thought of achieving your personal best.
Step into your best self is a phrase I am considering using.

Target Market(s)

People who are looking to create a massive change in their lives.

Industry/Entity Type

Life Coaching

Contact Information for Business Card

Summit Stride Coaching
Neil Corbett
Head Coach
email neil@velomira.com.au
Mob 0412 583 604

Logo styles of interest
Abstract Logo
Requirements
Must have
• I wouldlike to have a free introductory offer on the reverse side of the card.
It would read something like:
Is coaching for me/you?
Try a free 45 minute session.
Book now call or email for your appointment.

```html
<!DOCTYPE html>
<html lang="en">
<head>
<meta charset="utf-8">
<title>Summit Stride Coaching – Business Card</title>
<link rel="stylesheet" href="https://fonts.googleapis.com/css2?family=Cutive+Mono&family=Tinos:wght@400;700&family=Roboto:wght@300&display=swap">
<style>
  :root {
    --bg: #a0b8a8;
    --banner: #1a6e00;
    --ink-light: #a9c3b3;
    --tagline: #1f6b08;
    --figure-bright: #4cff00;
    --figure-deep: #2a9a00;
  }
  * { margin: 0; padding: 0; box-sizing: border-box; }
  html, body { width: 1200px; height: 693px; overflow: hidden; background: var(--bg); }
  .card { position: relative; width: 1200px; height: 693px; background: var(--bg); }
  .card-art { position: absolute; inset: 0; }
  .banner { fill: var(--banner); filter: url(#bannerShadow); }
  .divider { stroke: var(--ink-light); stroke-width: 3; }
  .tagline {
    font-family: "Tinos", serif;
    font-size: 25px;
    letter-spacing: 1px;
    fill: var(--tagline);
    filter: url(#taglineShadow);
  }
  .business-name {
    position: absolute;
    left: 74px;
    top: 312px;
    font-family: "Cutive Mono", monospace;
    font-size: 56px;
    line-height: 1.2;
    color: var(--ink-light);
    white-space: nowrap;
  }
  .business-name span { display: block; }
  .contact { position: absolute; left: 598px; color: var(--ink-light); line-height: 1; white-space: nowrap; }
  .contact span { position: absolute; left: 0; }
  .contact .name { top: 337px; font-family: "Cutive Mono", monospace; font-size: 27px; }
  .contact .role { top: 368px; font-family: "Tinos", serif; font-weight: 700; font-size: 19px; }
  .contact .email { top: 398px; font-family: "Tinos", serif; font-size: 23px; }
  .contact .phone { top: 431px; font-family: "Roboto", sans-serif; font-weight: 300; font-size: 25px; letter-spacing: 0.5px; }
</style>
</head>
<body>
<main class="card">
  <svg class="card-art" width="1200" height="693" viewBox="0 0 1200 693">
    <defs>
      <filter id="bannerShadow" x="-10%" y="-20%" width="120%" height="160%">
        <feDropShadow dx="4" dy="22" stdDeviation="14" flood-color="#142819" flood-opacity="0.6"/>
      </filter>
      <filter id="taglineShadow" x="-5%" y="-50%" width="110%" height="200%">
        <feDropShadow dx="2" dy="6" stdDeviation="4" flood-color="#142819" flood-opacity="0.45"/>
      </filter>
      <linearGradient id="figureTone" x1="0" y1="0" x2="1" y2="1">
        <stop offset="0" stop-color="#4cff00"/>
        <stop offset="1" stop-color="#2a9a00"/>
      </linearGradient>
      <path id="taglineArc" d="M732 540 Q942 502 1154 536"/>
    </defs>

    <path class="banner" d="M54 217 C260 232 420 280 640 286 C860 292 1000 262 1157 239 L1163 409 C1000 400 880 500 680 505 C470 510 260 465 56 463 Z"/>

    <line class="divider" x1="573" y1="313" x2="573" y2="480"/>

    <rect class="walking-figure" role="img" aria-label="Bright green striding walker illustration"
          x="943" y="178" width="210" height="312" rx="24" fill="url(#figureTone)"/>

    <text class="tagline"><textPath href="#taglineArc">STEP INTO YOUR BEST SELF</textPath></text>
  </svg>

  <h1 class="business-name">
    <span>SUMMIT STRIDE</span>
    <span>COACHING</span>
  </h1>

  <div class="contact">
    <span class="name">NEIL CORBETT</span>
    <span class="role">Head Coach</span>
    <span class="email">neil@velomira.com.au</span>
    <span class="phone">0412 583 604</span>
  </div>
</main>
</body>
</html>
```